Flyer-Design für Weihnachtsbäume als Dekoration
Zielgruppe
Wir bearbeiten Bleche nach Kundenvorgaben. Nebenbei stellen wir immer mal ein paar Dekoartikel
bzw. Sonderanfertigen her.
https://feinblechwerk-muster.de/
http://www.talbergwerk.de/
https://feinblechwerk-muster.de/aktuelles/image-broschuere/
Mit diesem Flyer wollen wir für unsere Weihnachtsbäume werben. Die Preise sind Endpreis inkl. Mehrwertsteuer.
Aufgabenstellung
Ich hab noch mehr Bildmaterial zur Verfügung.

```html
<!DOCTYPE html>
<html lang="de">
<head>
<meta charset="utf-8">
<title>Weihnachtsbäume – Varianten</title>
<link href="https://fonts.googleapis.com/css2?family=Kaushan+Script&family=Oswald:wght@500;600&family=Roboto+Condensed:wght@300&display=swap" rel="stylesheet">
<style>
  :root {
    --bg: #e9e9e9;
    --paper: #f7f7f7;
    --bronze: #b08d52;
    --bronze-dark: #9a7b45;
    --gold-light: #d3bd7c;
    --gold-mid: #c4ac66;
    --gold-text: #c9ad5c;
    --photo-dark: #2e2e2e;
    --photo-light: #9a9a9a;
    --white: #ffffff;
  }
  * { box-sizing: border-box; margin: 0; padding: 0; }
  html, body { width: 1200px; height: 800px; overflow: hidden; }
  body { background: var(--bg); position: relative; }

  .flyer {
    position: absolute; left: 250px; top: 50px;
    width: 700px; height: 700px;
    background: var(--paper);
    box-shadow: 0 6px 24px rgba(0,0,0,.12);
    overflow: hidden;
  }
  .top-band { position: absolute; left: 0; top: 0; width: 700px; height: 14px; background: var(--bronze); }
  .right-edge { position: absolute; right: 0; top: 14px; width: 14px; height: 570px; background: var(--bronze); }

  .price-photo {
    position: absolute; left: 0; top: 14px; width: 540px; height: 546px;
    background: radial-gradient(ellipse at 40% 35%, var(--gold-mid), var(--gold-light) 70%);
  }
  .tree-photo {
    position: absolute; left: 540px; top: 14px; width: 146px; height: 531px;
    background: linear-gradient(180deg, var(--photo-dark) 0%, var(--photo-light) 45%, var(--white) 60%, var(--photo-light) 100%);
  }
  .ribbon { position: absolute; left: 540px; top: 14px; width: 146px; height: 531px; }
  .vat-note {
    position: absolute; left: 572px; top: 118px; width: 170px;
    transform: rotate(-64deg); transform-origin: left top;
    font-family: "Roboto Condensed", sans-serif; font-weight: 300;
    font-size: 10.5px; line-height: 1.35; color: var(--white);
  }

  .variants { position: absolute; left: 56px; top: 60px; width: 468px; }
  .variants-title {
    font-family: "Kaushan Script", cursive; font-weight: 400;
    font-size: 34px; color: var(--white); margin-bottom: 8px;
  }
  .variant-row {
    display: grid; grid-template-columns: 1fr 96px 82px; align-items: end;
    height: 36px; padding-bottom: 4px;
    border-bottom: 1px solid var(--white);
    color: var(--white);
  }
  .variant-name, .variant-height {
    font-family: "Roboto Condensed", sans-serif; font-weight: 300; font-size: 12.5px;
  }
  .variant-price {
    font-family: "Oswald", sans-serif; font-weight: 600; font-size: 17px; text-align: right;
  }

  .web-box {
    position: absolute; left: 300px; top: 598px; width: 340px; height: 54px;
    border: 2px solid var(--gold-text);
    display: flex; align-items: center; justify-content: center;
    font-family: "Oswald", sans-serif; font-weight: 600; font-size: 24px;
    color: var(--gold-text); letter-spacing: .5px;
  }
</style>
</head>
<body>
  <article class="flyer">
    <div class="top-band"></div>
    <div class="price-photo" role="img" aria-label="Foto eines Metall-Weihnachtsbaums vor Bäumen, mit goldenem Farbschleier"></div>
    <div class="tree-photo" role="img" aria-label="Schwarz-weiß Foto eines weißen Blech-Weihnachtsbaums mit runden Ausschnitten"></div>
    <svg class="ribbon" viewBox="0 0 146 531" aria-hidden="true">
      <polygon points="106,0 146,0 146,40 60,230 20,230" fill="var(--bronze)"/>
      <polygon points="20,230 60,210 146,330 146,400" fill="var(--bronze-dark)"/>
    </svg>
    <p class="vat-note">Die Preise sind Endpreise<br>inkl. Mehrwertsteuer.</p>
    <div class="right-edge"></div>

    <section class="variants">
      <h1 class="variants-title">Varianten</h1>
      <div class="variant-row"><span class="variant-name">Baum, weiß beschichtet</span><span class="variant-height">Höhe: klein</span><span class="variant-price">25,00 €</span></div>
      <div class="variant-row"><span class="variant-name">Baum, weiß beschichtet</span><span class="variant-height">Höhe: 80cm</span><span class="variant-price">36,00 €</span></div>
      <div class="variant-row"><span class="variant-name">Baum, verzinkt</span><span class="variant-height">Höhe: 100cm</span><span class="variant-price">130,00 €</span></div>
      <div class="variant-row"><span class="variant-name">Baum, weiß beschichtet</span><span class="variant-height">Höhe: 120cm</span><span class="variant-price">90,00 €</span></div>
      <div class="variant-row"><span class="variant-name">Baum, verzinkt</span><span class="variant-height">Höhe: 120cm</span><span class="variant-price">150,00 €</span></div>
      <div class="variant-row"><span class="variant-name">Baum, doppelwandig, verzinkt</span><span class="variant-height">Höhe: 150cm</span><span class="variant-price">300,00 €</span></div>
      <div class="variant-row"><span class="variant-name">Baum, doppelwandig, verzinkt &amp; pulverbeschichtet</span><span class="variant-height">Höhe: 150cm</span><span class="variant-price">370,99 €</span></div>
      <div class="variant-row"><span class="variant-name">Baum, doppelwandig, Cortenstahl (Rostoptik)</span><span class="variant-height">Höhe: 150cm</span><span class="variant-price">335,00 €</span></div>
      <div class="variant-row"><span class="variant-name">Baum, doppelwandig, verzinkt</span><span class="variant-height">Höhe: 180cm</span><span class="variant-price">350,00 €</span></div>
      <div class="variant-row"><span class="variant-name">Baum, doppelwandig, verzinkt</span><span class="variant-height">Höhe: 230cm</span><span class="variant-price">430,00 €</span></div>
      <div class="variant-row"><span class="variant-name">Baum, doppelwandig, nicht verzinkt</span><span class="variant-height">Höhe: 230cm</span><span class="variant-price">280,00 €</span></div>
    </section>

    <div class="web-box">TALBERGWERK.DE</div>
  </article>
</body>
</html>
```